【 概要 】 自社メディアに誘導する広告バナーとサムネイルデザインを募集します。 【 依頼内容 】 ・サイズ: 横 × 縦1200×628 ・作成数: 1種類×1サイズ ★サムネイル用は参考画像があります。 ・利用用途:バナー広告 【 デザインイメージ 】 ・参考デザイン:検索エンジンに引っかからないようにするため、コメントにて記載Googleドキュメントのテキストにて添付いたします。 こちらより参考にしてくださいませ。 https://notes.pelvarix.net/document/d/7Qw3LmZr8TyUbXcVnK2sDfGhJp4Ae9RoWi61Lkuvzt_P/edit?usp=sharing 【 契約金額(税抜) 】 2,000円 ※契約金額(税込)からシステム利用料を差し引いた金額が、ワーカーさまの受取金額となります その他ご質問等ありましたら、気軽にお問い合わせください。 ご応募をお待ちしております! |
| https://hibikurashi.tane-kobora.jp/localblog/rivo_kayaking.html | ||

```html
<!DOCTYPE html>
<html lang="ja">
<head>
<meta charset="utf-8">
<title>30代からのオトナの停滞肌をレスキュー!</title>
<link rel="stylesheet" href="https://fonts.googleapis.com/css2?family=M+PLUS+Rounded+1c:wght@500;800;900&display=swap">
<style>
  :root {
    --photo-light: #f3f1ef;
    --photo-warm: #e9e3de;
    --photo-cool: #e6ebef;
    --photo-dark: #3b3634;
    --panel: rgba(255, 255, 255, 0.93);
    --panel-edge: #f2c9cf;
    --title-green: #1f5b3c;
    --title-red: #e3344b;
    --ink: #3a3a3a;
    --brand: #e8603a;
    --white: #ffffff;
  }
  * { margin: 0; padding: 0; box-sizing: border-box; }
  html, body { width: 1200px; height: 628px; overflow: hidden; background: var(--white); }
  .banner {
    position: relative;
    width: 1200px;
    height: 628px;
    overflow: hidden;
    font-family: "M PLUS Rounded 1c", sans-serif;
    background: var(--photo-light);
  }
  .photo { position: absolute; }
  .photo--mirror-left {
    left: 0; top: 0; width: 300px; height: 390px;
    background: linear-gradient(160deg, #d9d6d3 0%, #f4f2f0 45%, #cfcac6 100%);
  }
  .photo--counsel-center {
    left: 300px; top: 0; width: 560px; height: 110px;
    background: linear-gradient(90deg, #eeeceb 0%, #f8f7f6 55%, #ebe7e4 100%);
  }
  .photo--mirror-right {
    left: 860px; top: 0; width: 340px; height: 250px;
    background: linear-gradient(200deg, #f6f7f8 0%, var(--photo-cool) 60%, #dcdad8 100%);
  }
  .photo--products {
    left: 0; top: 390px; width: 470px; height: 238px;
    background: linear-gradient(180deg, #b99a86 0%, #e7ded8 40%, #f7f5f3 100%);
  }
  .photo--staff-right {
    left: 760px; top: 250px; width: 440px; height: 378px;
    background: linear-gradient(160deg, #f7f7f7 0%, #eceff2 50%, #d9d4d1 100%);
  }
  .photo--center-bottom {
    left: 470px; top: 410px; width: 290px; height: 218px;
    background: linear-gradient(180deg, #f2f0ee 0%, #fafafa 100%);
  }
  .panel {
    position: absolute;
    left: 290px; top: 98px;
    width: 620px; height: 322px;
  }
  .panel svg { position: absolute; inset: 0; }
  .tab {
    position: absolute;
    left: 395px; top: 66px;
    width: 410px; height: 40px;
    background: var(--panel);
    border-radius: 20px 20px 0 0;
    display: flex; align-items: center; justify-content: center;
    font-size: 20px; font-weight: 800; color: var(--ink);
    letter-spacing: 0.02em;
  }
  .headline {
    position: absolute;
    left: 0; top: 150px; width: 1200px;
    text-align: center;
    font-weight: 900;
    line-height: 1;
    color: var(--title-green);
    paint-order: stroke fill;
    -webkit-text-stroke: 6px var(--white);
  }
  .headline__line { display: block; }
  .headline__lead { font-size: 46px; margin-bottom: 18px; }
  .headline__concerns { font-size: 62px; margin-bottom: 18px; letter-spacing: 0.01em; }
  .headline__subject { font-size: 52px; margin-bottom: 16px; }
  .headline__action { font-size: 86px; color: var(--title-red); letter-spacing: 0.06em; }
  .media {
    position: absolute;
    left: 470px; top: 468px; width: 260px;
    text-align: center;
  }
  .media__tagline { font-size: 12px; font-weight: 500; color: var(--ink); line-height: 1.4; text-align: left; padding-left: 14px; }
  .media__name { margin-top: 8px; font-size: 44px; font-weight: 800; color: var(--brand); letter-spacing: 0.04em; line-height: 1; }
</style>
</head>
<body>
  <main class="banner">
    <div class="photo photo--mirror-left" role="img" aria-label="鏡の前でメイクを受ける女性の後ろ姿の写真"></div>
    <div class="photo photo--counsel-center" role="img" aria-label="カウンセリング中の美容スタッフの写真"></div>
    <div class="photo photo--mirror-right" role="img" aria-label="鏡に映る美容スタッフの写真"></div>
    <div class="photo photo--products" role="img" aria-label="白いスキンケアボトルとクリームジャーが並ぶ棚の写真"></div>
    <div class="photo photo--center-bottom" role="img" aria-label="製品を手で示す店内の写真"></div>
    <div class="photo photo--staff-right" role="img" aria-label="赤いスカーフを付けた笑顔の美容スタッフの写真"></div>

    <div class="panel">
      <svg width="620" height="322" viewBox="0 0 620 322" aria-hidden="true">
        <path d="M24 0 H596 A24 24 0 0 0 620 24 V298 A24 24 0 0 0 596 322 H24 A24 24 0 0 0 0 298 V24 A24 24 0 0 0 24 0 Z"
              fill="rgba(255,255,255,0.93)" stroke="#f2c9cf" stroke-width="2"/>
      </svg>
    </div>
    <div class="tab">ルミナ化粧品さんに聞いてみた!</div>

    <h1 class="headline">
      <span class="headline__line headline__lead">30代からの</span>
      <span class="headline__line headline__concerns">乾燥・くすみ・たるみ…</span>
      <span class="headline__line headline__subject">オトナの停滞肌を</span>
      <span class="headline__line headline__action">レスキュー!</span>
    </h1>

    <div class="media">
      <p class="media__tagline">北陸で働く女性を笑顔にする<br>コワーキングメディア</p>
      <p class="media__name">ヒビクラシ</p>
    </div>
  </main>
</body>
</html>
```